SEAFOOD PACKAGING (Products for consumer)

We are looking to create packaging for various seafood products such as octopus and squid. We plan to sell our products in upscale supermarkets.

We are specializing in cut octopus this time.

Please include our company logo. Also, please leave a transparent area so that customers can see the product inside.
Updates

We want to show what is inside, so a picture of the octopus is not required. We need something simple and sophisticated.

Target Market(s)

upscale store in US and ASIA

Industry/Entity Type

Fisheries dealer

Requirements
Must have
• Please include the attached logo,Blue one is preferred.Please leave a transparent part so that the contents of the product can be seen by the consumer.1. product name on packaging →CUT OCTOPUS,TAKO SASHIMI,Highest quality,Top quality etc... 3. What text information should be on the packaging →(It may be edited, but this is the image) The raw materials are caught in a very clean environment and processed in a modern factory with ZEK certification. We are committed to additive-free products. 4. Packing size(cm/inch)→it will be about 19cm*22cm. 5. what kind of packaging do you use →PP or PA 6. dll →ai,jag
Nice to have
• https://quillmora.example/shots/4829174-Velka-Reef We need something simple and sophisticated like this one.
Should not have
• We want to show what is inside, so a picture of the octopus is not required. We need something simple and sophisticated.

```html
<!DOCTYPE html>
<html lang="en">
<head>
<meta charset="utf-8">
<title>Marevo Cut Octopus Package</title>
<link rel="stylesheet" href="https://fonts.googleapis.com/css2?family=Oswald:wght@400;500;600&family=Roboto+Condensed:wght@500;600&display=swap">
<style>
  :root {
    --backdrop: #97ccf2;
    --label-white: #f3f4f6;
    --seal-white: #e9ecef;
    --window-blue: #a9d4f4;
    --brand-blue: #4466a6;
    --navy: #1f3a7c;
    --deep-blue: #1d3a82;
    --mid-blue: #4f74b4;
    --red-dark: #b3202a;
    --red-soft: #d05a66;
    --line-red: #c8323c;
    --text-light: #e6ecf7;
  }
  * { margin: 0; padding: 0; box-sizing: border-box; }
  html, body { width: 1200px; height: 1200px; overflow: hidden; background: var(--backdrop); }
  .canvas { position: relative; width: 1200px; height: 1200px; }
  .bag {
    position: absolute; left: 213px; top: 163px; width: 740px; height: 852px;
    overflow: hidden;
  }
  .label {
    position: absolute; left: 0; top: 0; width: 470px; height: 852px;
    background: var(--label-white);
  }
  .window {
    position: absolute; left: 470px; top: 0; width: 270px; height: 852px;
    background: var(--window-blue);
  }
  .product-view {
    position: absolute; left: 0; top: 92px; width: 255px; height: 714px;
    border-radius: 0 110px 120px 0;
    background: linear-gradient(160deg, #d9b2ab 0%, #ecd0c9 40%, #e6c2ba 70%, #d7a9a1 100%);
  }
  .seal { position: absolute; left: 0; width: 740px; height: 44px; }
  .seal-top { top: 0; }
  .seal-bottom { bottom: 0; }
  .seal-top .seal-label { background: repeating-linear-gradient(90deg, var(--seal-white) 0 4px, #ffffff 4px 7px); }
  .seal-bottom .seal-label { background: repeating-linear-gradient(90deg, #1f3d86 0 4px, #2d4d97 4px 7px); }
  .seal-label { position: absolute; left: 0; top: 0; width: 470px; height: 100%; }
  .seal-window { position: absolute; left: 470px; top: 0; width: 270px; height: 100%;
    background: repeating-linear-gradient(90deg, #9ccbf0 0 4px, #b2d9f6 4px 7px); }

  .brand {
    position: absolute; left: 0; width: 470px; top: 165px; text-align: center;
  }
  .brand-dot {
    display: block; width: 70px; height: 70px; margin: 0 auto 22px;
    border-radius: 50%; background: var(--brand-blue);
  }
  .brand-name {
    font-family: "Oswald", sans-serif; font-weight: 600; font-size: 58px;
    letter-spacing: 8px; color: var(--brand-blue); line-height: 1;
  }
  .product-name {
    position: absolute; left: 0; width: 470px; top: 318px; text-align: center;
    font-family: "Oswald", sans-serif; font-weight: 600; font-size: 72px; line-height: 1;
    letter-spacing: 1px;
  }
  .product-name .cut { color: var(--red-dark); }
  .product-name .octopus { color: var(--red-soft); }
  .subtitle {
    position: absolute; left: 55px; width: 360px; top: 404px;
    display: flex; align-items: center; gap: 14px;
    font-family: "Oswald", sans-serif; font-weight: 500; font-size: 40px; color: var(--navy);
    white-space: nowrap;
  }
  .subtitle::before, .subtitle::after { content: ""; flex: 1; height: 3px; background: var(--line-red); }

  .sea {
    position: absolute; left: 0; top: 440px; width: 470px; height: 400px;
  }
  .claims {
    position: absolute; left: 37px; top: 641px; width: 395px; height: 80px;
    border: 1.5px solid var(--line-red); border-top: none;
  }
  .claims-title {
    position: absolute; left: 0; right: 0; top: -11px; display: flex; align-items: center; gap: 8px;
    font-family: "Roboto Condensed", sans-serif; font-weight: 600; font-size: 15.5px;
    color: var(--text-light); white-space: nowrap;
  }
  .claims-title::before, .claims-title::after { content: ""; flex: 1; height: 1.5px; background: var(--line-red); }
  .claims-body {
    position: absolute; left: 0; right: 0; top: 20px; text-align: center;
    font-family: "Roboto Condensed", sans-serif; font-weight: 500; font-size: 10.6px;
    line-height: 15.5px; color: var(--text-light);
  }
  .storage {
    position: absolute; left: 0; width: 470px; top: 760px; text-align: center;
    font-family: "Roboto Condensed", sans-serif; font-weight: 500; font-size: 11px;
    line-height: 20px; color: var(--text-light); letter-spacing: 0.3px;
  }
</style>
</head>
<body>
<div class="canvas">
  <div class="bag">
    <div class="label">
      <div class="brand">
        <span class="brand-dot"></span>
        <div class="brand-name">MAREVO</div>
      </div>
      <div class="product-name"><span class="cut">CUT</span> <span class="octopus">OCTOPUS</span></div>
      <div class="subtitle">TAKO SASHIMI</div>

      <svg class="sea" viewBox="0 0 470 400" role="img" aria-label="Layered blue sea waves with silhouettes of seaweed and coral on the seabed">
        <defs>
          <linearGradient id="seaDepth" x1="0" y1="0" x2="0" y2="1">
            <stop offset="0" stop-color="#3a64ab"/>
            <stop offset="1" stop-color="#1b3a86"/>
          </linearGradient>
        </defs>
        <path d="M0 180 C 110 150 200 210 300 185 C 380 165 430 180 470 175 L470 400 L0 400 Z" fill="#5f86c2" opacity="0.55"/>
        <path d="M0 190 C 120 175 200 205 300 195 C 380 185 430 200 470 190 L470 400 L0 400 Z" fill="url(#seaDepth)"/>
        <path d="M0 185 C 90 205 160 215 250 205 C 330 196 400 215 470 210 L470 260 L0 260 Z" fill="#6f8fc6" opacity="0.6"/>
        <path d="M0 235 C 100 255 200 250 300 240 C 380 232 430 245 470 240 L470 400 L0 400 Z" fill="#1f3e88"/>
      </svg>

      <div class="claims">
        <div class="claims-title">ALL NATURAL • HIGHEST QUALITY • TOP QUALITY</div>
        <p class="claims-body">THE RAW MATERIALS ARE CAUGHT IN A VERY CLEAN ENVIRONMENT<br>AND PROCESSED IN A MODERN FACTORY WITH ZEK CERTIFICATION.<br>WE ARE COMMITTED TO ADDITIVE-FREE PRODUCTS.</p>
      </div>
      <div class="storage">KEEP FROZEN, NO PRESERVATIVES<br>NET. WT 1 LB (500 G)</div>
    </div>

    <div class="window">
      <div class="product-view" role="img" aria-label="Frozen cut octopus tentacles visible through the clear window"></div>
    </div>

    <div class="seal seal-top"><div class="seal-label"></div><div class="seal-window"></div></div>
    <div class="seal seal-bottom"><div class="seal-label"></div><div class="seal-window"></div></div>
  </div>
</div>
</body>
</html>
```